Letterhead for SaaS

Design a letterhead that aligns with our new business card, using our logo and color scheme and text defined in the Branding Guide to ensure consistency. Consider incorporating a subtle watermark for added elegance. The layout should reflect the card's style, creating a cohesive look across our stationery.

```html
<!DOCTYPE html>
<html lang="en">
<head>
<meta charset="utf-8">
<title>Vantoria Letterhead</title>
<link rel="stylesheet" href="https://fonts.googleapis.com/css2?family=Saira:wght@700&family=Montserrat:wght@400;600&display=swap">
<style>
  :root {
    --navy: #141b2d;
    --navy-deep: #0e1422;
    --sky: #3bb8ea;
    --paper: #ffffff;
    --ink: #1a1f2b;
    --backdrop: #e2e2e2;
    --watermark: #f4f4f4;
  }
  html, body {
    margin: 0;
    padding: 0;
    width: 1174px;
    height: 1200px;
    overflow: hidden;
    background: var(--backdrop);
  }
  .letterhead {
    position: absolute;
    left: 143px;
    top: 30px;
    width: 887px;
    height: 1140px;
    background: var(--paper);
    box-shadow: 0 6px 18px rgba(0,0,0,0.18);
  }
  .letterhead svg { display: block; width: 100%; height: 100%; }
  .brand-name { font-family: "Saira", sans-serif; font-weight: 700; }
  .contact-text { font-family: "Montserrat", sans-serif; font-weight: 400; fill: var(--ink); font-size: 22px; }
  .navy-fill { fill: var(--navy); }
  .sky-fill { fill: var(--sky); }
  .paper-fill { fill: var(--paper); }
</style>
</head>
<body>
<div class="letterhead">
  <svg viewBox="0 0 1264 1625" xmlns="http://www.w3.org/2000/svg">
    <!-- header band -->
    <rect class="navy-fill" x="0" y="0" width="1264" height="330"/>
    <path class="sky-fill" d="M0,205 C380,60 880,40 1264,72 L1264,330 L0,330 Z"/>
    <path class="paper-fill" d="M0,262 C400,95 880,58 1264,78 L1264,330 L0,330 Z"/>
    <path class="paper-fill" d="M700,80 C900,45 1100,40 1240,70 C1100,52 900,55 700,88 Z"/>

    <!-- logo spot: name with a plain square -->
    <rect class="sky-fill" x="118" y="92" width="26" height="26"/>
    <text class="brand-name" x="156" y="118" font-size="34" fill="#ffffff">VANTORIA</text>

    <!-- contact block -->
    <rect x="908" y="100" width="2" height="145" fill="var(--ink)"/>
    <text class="brand-name" x="926" y="136" font-size="46" fill="var(--navy)">VANTORIA</text>

    <!-- phone icon -->
    <path class="sky-fill" d="M929,163 q9,-6 18,0 l-2,4 h-4 l-1,-2 q-2,-1 -4,0 l-1,2 h-4 Z M930,170 h16 l-2,7 h-12 Z"/>
    <text class="contact-text" x="957" y="179">(555) 014-2290</text>

    <!-- mail icon -->
    <rect class="sky-fill" x="929" y="197" width="18" height="12"/>
    <path d="M929,197 L938,205 L947,197" fill="none" stroke="#ffffff" stroke-width="1.5"/>
    <text class="contact-text" x="957" y="210">info@vantoria.com</text>

    <!-- globe icon -->
    <circle class="sky-fill" cx="938" cy="233" r="9"/>
    <path d="M929,233 h18 M938,224 q-6,9 0,18 M938,224 q6,9 0,18" fill="none" stroke="#ffffff" stroke-width="1.2"/>
    <text class="contact-text" x="957" y="241">www.vantoria.com</text>

    <!-- header rules -->
    <rect x="78" y="289" width="1108" height="2" fill="var(--ink)"/>
    <rect x="78" y="296" width="1108" height="2" class="sky-fill"/>

    <!-- faint watermark name -->
    <text class="brand-name" x="632" y="870" font-size="170" text-anchor="middle" fill="var(--watermark)">VANTORIA</text>

    <!-- footer band -->
    <path class="sky-fill" d="M60,1552 C520,1592 1000,1530 1264,1398 L1264,1445 C1000,1560 520,1605 60,1552 Z"/>
    <path class="navy-fill" d="M0,1546 C520,1606 1000,1565 1264,1458 L1264,1625 L0,1625 Z"/>
  </svg>
</div>
</body>
</html>
```